This is a label for a new sake made in Japan imported into Aust

This will be a bottle label for a new sake imported into Australia. The hero of the label is the Velmora. We have joined the "O" meaning great in Japanese and used sake with "Z" to have Velmora with the play on words using Oz as in our slang for Aussie. A modern label with a Japanese take is key. This is a premium sake made in Japan for the Australian market.
The "Tall Casks" up the top is the name of the company, we have yet to design a logo for the company.

Target Market(s)

Alcohol

Logo Text

Velmora

Font styles to use
Serif

Requirements
Must have
• easy to read, with a hint of Japanese origin
Should not have
• too busy

```html
<!DOCTYPE html>
<html lang="en">
<head>
<meta charset="utf-8">
<title>Velmora — Premium Japanese Sake Label</title>
<link rel="stylesheet" href="https://fonts.googleapis.com/css2?family=Cabin:wght@500&family=Oswald:wght@400;600&family=Roboto:wght@400&display=swap">
<style>
  :root {
    --backdrop: #dccbb2;
    --label-slate: #474b52;
    --label-slate-deep: #3f4349;
    --mist: #adb4c0;
    --paper-white: #ffffff;
  }
  html, body {
    margin: 0;
    padding: 0;
    width: 1200px;
    height: 800px;
    overflow: hidden;
    background: var(--backdrop);
  }
  .canvas {
    position: relative;
    width: 1200px;
    height: 800px;
    background: var(--backdrop);
  }
  .label {
    position: absolute;
    left: 0;
    top: 0;
    width: 632px;
    height: 800px;
    background: linear-gradient(180deg, var(--label-slate) 0%, var(--label-slate) 55%, var(--label-slate-deep) 80%, var(--label-slate) 100%);
  }
  .company-name {
    position: absolute;
    top: 88px;
    left: 0;
    width: 632px;
    text-align: center;
    font-family: "Cabin", sans-serif;
    font-weight: 500;
    font-size: 30px;
    letter-spacing: 1px;
    color: var(--mist);
    margin: 0;
  }
  .brand-ring {
    position: absolute;
    left: 118px;
    top: 242px;
    width: 370px;
    height: 370px;
  }
  .brand-name {
    position: absolute;
    top: 378px;
    left: 0;
    width: 606px;
    text-align: center;
    font-family: "Oswald", sans-serif;
    font-weight: 600;
    font-size: 74px;
    line-height: 1;
    color: var(--paper-white);
    margin: 0;
  }
  .tagline {
    position: absolute;
    top: 468px;
    left: 0;
    width: 632px;
    text-align: center;
    font-family: "Oswald", sans-serif;
    font-weight: 400;
    font-size: 23px;
    letter-spacing: -0.3px;
    color: var(--mist);
    margin: 0;
  }
  .footnote {
    position: absolute;
    top: 766px;
    left: 0;
    width: 632px;
    text-align: center;
    font-family: "Roboto", sans-serif;
    font-size: 15px;
    color: var(--mist);
    margin: 0;
  }
</style>
</head>
<body>
  <main class="canvas">
    <section class="label">
      <p class="company-name">TALL CASKS</p>
      <svg class="brand-ring" viewBox="0 0 370 370" aria-hidden="true">
        <circle cx="185" cy="185" r="176" fill="none" stroke="var(--mist)" stroke-width="10"/>
      </svg>
      <h1 class="brand-name">VELMORA</h1>
      <p class="tagline">PREMIUM JAPANESE SAKE</p>
      <p class="footnote">Lorem ipsum dolor</p>
    </section>
  </main>
</body>
</html>
```